Harlow Grading LLC business card design

Excavation company business cards

Contact Information for Business Card

Harlow Grading LLC cell phone 208-471-9360 office phone 208-396-4815 harlowgradingllc@mailverde.net Driveways, site prep, retaining walls, septic systems, rock delivery

Colors

Designer to choose colors to be used in the design.

```html
<!DOCTYPE html>
<html lang="en">
<head>
<meta charset="utf-8">
<title>Harlow Grading LLC – Business Card</title>
<link rel="stylesheet" href="https://fonts.googleapis.com/css2?family=Arimo:wght@400;700&display=swap">
<style>
  :root {
    --page: #e9e9e9;
    --card: #2e2e30;
    --card-deep: #242426;
    --ink: #f2f2f2;
    --ink-soft: #cfcfcf;
    --accent: #f07a22;
    --rule: #77777a;
  }
  * { box-sizing: border-box; margin: 0; padding: 0; }
  html, body {
    width: 1200px; height: 802px; overflow: hidden;
    background: var(--page);
    font-family: "Arimo", Arial, sans-serif;
  }
  .sheet {
    width: 1200px; height: 802px;
    display: flex; align-items: center; justify-content: center; gap: 56px;
  }
  .card {
    position: relative;
    width: 520px; height: 297px;
    background: var(--card);
    border-radius: 3px;
    box-shadow: 0 10px 24px rgba(0,0,0,.18);
    overflow: hidden;
    color: var(--ink);
  }

  /* Front */
  .brand {
    position: absolute; left: 78px; top: 104px;
    display: flex; align-items: center; gap: 10px;
  }
  .brand-mark { width: 16px; height: 16px; background: var(--accent); }
  .brand-name {
    font-weight: 700; font-size: 21px; letter-spacing: .5px;
    color: var(--accent); text-transform: uppercase; line-height: 1.1;
    width: 150px;
  }
  .divider {
    position: absolute; left: 272px; top: 96px;
    width: 1px; height: 78px; background: var(--rule);
  }
  .contacts {
    position: absolute; left: 292px; top: 100px;
    list-style: none; font-size: 14px; line-height: 24px; color: var(--ink);
  }
  .contacts li { display: flex; align-items: center; gap: 9px; }
  .contacts svg { width: 13px; height: 13px; flex: none; }
  .person {
    position: absolute; right: 262px; top: 190px; text-align: right;
  }
  .person-name {
    font-size: 16px; font-weight: 400; color: var(--accent);
    letter-spacing: .6px; text-transform: uppercase;
  }
  .person-role { font-size: 14px; color: var(--ink); margin-top: 3px; }

  /* Back */
  .back-brand {
    position: absolute; left: 30px; top: 30px;
    display: flex; align-items: center; gap: 8px;
  }
  .back-brand .brand-mark { width: 12px; height: 12px; }
  .back-brand .brand-name { font-size: 16px; width: auto; }
  .services {
    position: absolute; left: 30px; top: 100px;
    list-style: none; font-size: 17px; line-height: 29px;
    color: var(--ink-soft); text-transform: uppercase; letter-spacing: .3px;
  }
  .services li { display: flex; align-items: center; gap: 10px; }
  .services li::before {
    content: ""; width: 7px; height: 7px; border-radius: 50%;
    background: var(--accent); flex: none;
  }
  .machine-art {
    position: absolute; right: 0; top: 0;
    width: 290px; height: 297px;
    background: linear-gradient(135deg, #3a3a3c 0%, #1c1c1d 55%, #4a4a4c 100%);
    clip-path: polygon(40% 0, 100% 0, 100% 100%, 0 100%, 10% 70%, 22% 45%);
  }
</style>
</head>
<body>
<main class="sheet">
  <section class="card card-front" aria-label="Card front">
    <div class="brand">
      <span class="brand-mark"></span>
      <span class="brand-name">Harlow Grading LLC</span>
    </div>
    <div class="divider"></div>
    <ul class="contacts">
      <li>
        <svg viewBox="0 0 16 16" fill="none" stroke="var(--accent)" stroke-width="1.6"><rect x="4" y="1" width="8" height="14" rx="1.5"/><line x1="7" y1="12.5" x2="9" y2="12.5"/></svg>
        208-471-9360
      </li>
      <li>
        <svg viewBox="0 0 16 16" fill="var(--accent)"><path d="M3.5 1.5l2.5 0 1 3.5-1.6 1.2a8 8 0 0 0 4.4 4.4L11 9l3.5 1v2.5c0 1-1 2-2 2C6.5 14.5 1.5 9.5 1.5 3.5c0-1 1-2 2-2z"/></svg>
        208-396-4815
      </li>
      <li>
        <svg viewBox="0 0 16 16" fill="var(--accent)"><path d="M1 3h14v10H1z"/><path d="M1 3l7 6 7-6" fill="none" stroke="var(--card)" stroke-width="1.4"/></svg>
        harlowgradingllc@mailverde.net
      </li>
    </ul>
    <div class="person">
      <p class="person-name">Marcus Reilly</p>
      <p class="person-role">Manager</p>
    </div>
  </section>

  <section class="card card-back" aria-label="Card back">
    <div class="back-brand">
      <span class="brand-mark"></span>
      <span class="brand-name">Harlow Grading LLC</span>
    </div>
    <ul class="services">
      <li>Driveways</li>
      <li>Site Prep</li>
      <li>Retaining Walls</li>
      <li>Septic Systems</li>
      <li>Rock Delivery</li>
    </ul>
    <div class="machine-art" role="img" aria-label="Embossed dark illustration of an excavator in front of mountain peaks"></div>
  </section>
</main>
</body>
</html>
```